AUSTRALIAN CONSULTING FIRM BUSINESS CARD - MODERN

We are wanting a modern, clean lined business card design. We are professional niche consultancy firm situated in Australia called Marlow Advisory Partners Pty Ltd.
The card should communicate professionalism and creativity and draw on our logo design (attached).
The design should be two sided, landscape orientation.
Target Market(s)
government, not for profit sector, corporate clients
Industry/Entity Type
Landscape
Requirements
Must have
- logo
no new introduced colours

```html
<!DOCTYPE html>
<html lang="en">
<head>
<meta charset="utf-8">
<title>Marlow Advisory Partners – Business Card Set</title>
<link rel="stylesheet" href="https://fonts.googleapis.com/css2?family=Open+Sans:wght@400;600;700&display=swap">
<style>
  :root {
    --backdrop: #4a4d52;
    --label: #f2f2f2;
    --card-white: #ffffff;
    --brand-blue: #1f3f9b;
    --brand-sky: #2d8fd6;
    --brand-purple: #9b3b9f;
    --brand-green: #35a845;
    --brand-lime: #a6d23c;
    --text-dark: #333333;
  }
  * { box-sizing: border-box; margin: 0; padding: 0; }
  html, body {
    width: 1200px; height: 566px; overflow: hidden;
    background: var(--backdrop);
    font-family: "Open Sans", Arial, sans-serif;
  }
  .sheet { position: relative; width: 1200px; height: 566px; }

  .card-label {
    position: absolute; width: 330px; text-align: center;
    color: var(--label); font-size: 24px; font-weight: 400;
  }
  .card {
    position: absolute; width: 330px; height: 190px;
    background: var(--card-white); overflow: hidden;
    box-shadow: 0 6px 16px rgba(0,0,0,.35);
  }
  .col-left { left: 200px; }
  .col-right { left: 670px; }
  .row-top-label { top: 36px; }
  .row-top { top: 74px; }
  .row-bottom-label { top: 292px; }
  .row-bottom { top: 330px; }

  .brand-name {
    color: var(--brand-blue); font-weight: 700;
    line-height: 1.15; display: flex; align-items: center; gap: 8px;
  }
  .brand-dot {
    width: 12px; height: 12px; border-radius: 50%;
    background: var(--brand-green); flex: none;
  }

  /* Front */
  .front .brand-name { position: absolute; left: 18px; top: 18px; font-size: 14px; width: 220px; }
  .front .person { position: absolute; left: 60px; top: 64px; font-size: 12px; color: var(--brand-blue); font-weight: 700; }
  .front .person span { font-weight: 400; color: var(--text-dark); font-size: 10px; }
  .front .contacts { position: absolute; left: 64px; top: 86px; list-style: none; font-size: 9px; color: var(--text-dark); }
  .front .contacts li { display: flex; align-items: center; gap: 5px; height: 13px; }
  .front .contacts svg { width: 8px; height: 8px; fill: var(--brand-blue); }
  .front .address { position: absolute; left: 64px; top: 146px; font-size: 9.5px; color: var(--text-dark); line-height: 1.35; }
  .front .swoosh { position: absolute; inset: 0; }

  /* Back-1 */
  .back-one .brand-name { position: absolute; left: 22px; top: 40px; font-size: 20px; width: 280px; }
  .back-one .site { position: absolute; right: 22px; bottom: 22px; font-size: 13px; color: var(--text-dark); }

  /* Back-2 */
  .back-two { background: linear-gradient(90deg, var(--brand-green) 0%, var(--brand-green) 40%, var(--brand-lime) 100%); }
  .back-two .brand-name { position: absolute; left: 30px; top: 66px; font-size: 20px; width: 280px; }

  /* Back-3 */
  .back-three .brand-name { position: absolute; left: 30px; top: 50px; font-size: 20px; width: 280px; }
  .back-three .site { position: absolute; left: 0; right: 0; bottom: 30px; text-align: center; font-size: 12px; color: var(--text-dark); }
</style>
</head>
<body>
<main class="sheet">

  <p class="card-label col-left row-top-label">Front</p>
  <section class="card front col-left row-top" aria-label="Card front">
    <svg class="swoosh" viewBox="0 0 330 190" aria-hidden="true">
      <path d="M330 30 C300 90 250 160 150 190 L330 190 Z" fill="var(--brand-green)"/>
      <path d="M330 10 C290 90 240 160 170 190 L330 190 Z" fill="var(--brand-blue)"/>
      <path d="M330 60 C310 120 270 170 230 190 L330 190 Z" fill="var(--brand-green)"/>
    </svg>
    <div class="brand-name"><span class="brand-dot"></span>Marlow Advisory Partners Pty Ltd</div>
    <p class="person">Your Name<span>, Designation</span></p>
    <ul class="contacts">
      <li><svg viewBox="0 0 10 10"><path d="M2 0h3l1 3-2 1a6 6 0 0 0 2 2l1-2 3 1v3H8A8 8 0 0 1 0 2V0z"/></svg>0 123 456 789</li>
      <li><svg viewBox="0 0 10 10"><circle cx="5" cy="5" r="5"/></svg>0 123 456 789</li>
      <li><svg viewBox="0 0 10 10"><path d="M0 2h10v6H0z M0 2l5 3 5-3" stroke="#fff" stroke-width=".8"/></svg>email@website.com</li>
      <li><svg viewBox="0 0 10 10"><circle cx="5" cy="5" r="4.5" fill="none" stroke="var(--brand-blue)"/><path d="M0.5 5h9M5 .5v9" stroke="var(--brand-blue)" stroke-width=".8"/></svg>www.website.com</li>
    </ul>
    <p class="address">Suite 0000, Street Name<br>city Name, Country Code</p>
  </section>

  <p class="card-label col-left row-bottom-label">Back-1</p>
  <section class="card back-one col-left row-bottom" aria-label="Card back option one">
    <div class="brand-name"><span class="brand-dot"></span>Marlow Advisory Partners Pty Ltd</div>
    <p class="site">www.yourwebsite.com</p>
  </section>

  <p class="card-label col-right row-top-label">Back-2</p>
  <section class="card back-two col-right row-top" aria-label="Card back option two">
    <div class="brand-name"><span class="brand-dot" style="background: var(--card-white)"></span>Marlow Advisory Partners Pty Ltd</div>
  </section>

  <p class="card-label col-right row-bottom-label">Back-3</p>
  <section class="card back-three col-right row-bottom" aria-label="Card back option three">
    <div class="brand-name"><span class="brand-dot"></span>Marlow Advisory Partners Pty Ltd</div>
    <p class="site">www.yourwebsite.com</p>
  </section>

</main>
</body>
</html>
```